Recruitment Agency Needs a Core Values Wall for Office

Hello! We are hoping to reach out to the designer community to help us with achieving a wall in our office that beautifully presents our core values, so thanks for stopping by!
We are in a corporate office, but our median age in the office is 28 years old. For this reason we want the design to be fun, young and colourful while showing some sophistication.
The wall will be visible to the staff (within the open plan office), and the right colours will need to be used to enhance mood and productivity. Perhaps we could be looking at a colour for each core value? Or potentially some other way for each value to stand out?
The background doesn't have to be a specific colour. We would like some options to see how it will reflect in the office.
In terms of size - we aren't 100% on what size we are wanting to do it... but work within 1500x2700mm and we can work off that.
Fonts can be experimented with, without being too overpowering to the eye.
It needs to be clear, punchy and stand out from across the office (while being easy on the eye).
I have attached two images that can be used as inspiration. We would like more colour throughout the design.
The core values that will be required to be displayed:
Stop. Think. Challenge the Norm.
Our Detail is Our Difference.
Best Intentions. ALWAYS.
Turn Up, Turn On! Make ..it Happen!
Support Like Family. Party Like Rockstars.
Target Market(s)
Median staff age of 28, corporate office
Industry/Entity Type
Recruitment
Colors
Designer to choose colors to be used in the design.

```html
<!DOCTYPE html>
<html lang="en">
<head>
<meta charset="utf-8">
<title>Core Values Wall</title>
<link rel="stylesheet" href="https://fonts.googleapis.com/css2?family=Stardos+Stencil:wght@700&family=Federo&family=Alfa+Slab+One&family=Audiowide&family=Lobster+Two:ital,wght@1,700&family=Sancreek&display=swap">
<style>
  :root {
    --wall: #b1bb75;
    --ink: #fdfbe3;
    --value-challenge: #a8352a;
    --value-detail: #fdfbe3;
    --value-intentions: #24506e;
    --value-happen: #6a2c5e;
    --value-support: #d9622b;
    --value-party: #fdfbe3;
  }
  html, body {
    margin: 0;
    padding: 0;
    width: 844px;
    height: 1200px;
    overflow: hidden;
    background: var(--wall);
  }
  .values-wall {
    display: block;
    width: 844px;
    height: 1200px;
  }
  .rule { stroke: var(--ink); stroke-width: 3; fill: none; }
  .motif { fill: var(--ink); }
  .value-stencil { font-family: "Stardos Stencil", sans-serif; font-weight: 700; fill: var(--value-challenge); }
  .value-light { font-family: "Federo", sans-serif; fill: var(--value-detail); }
  .value-slab { font-family: "Alfa Slab One", serif; fill: var(--value-detail); }
  .value-bold { font-family: "Alfa Slab One", serif; fill: var(--value-intentions); }
  .value-tech { font-family: "Audiowide", sans-serif; fill: var(--value-happen); }
  .value-script { font-family: "Lobster Two", cursive; font-style: italic; font-weight: 700; fill: var(--value-support); }
  .value-western { font-family: "Sancreek", serif; fill: var(--value-party); }
</style>
</head>
<body>
<svg class="values-wall" viewBox="0 0 844 1200" xmlns="http://www.w3.org/2000/svg">
  <!-- Stop. Think. -->
  <line class="rule" x1="106" y1="66" x2="727" y2="66"/>
  <text class="value-stencil" x="94" y="154" font-size="92" textLength="663" lengthAdjust="spacingAndGlyphs">STOP. THINK.</text>
  <text class="value-stencil" x="96" y="217" font-size="55" textLength="635" lengthAdjust="spacingAndGlyphs">CHALLENGE THE NORM.</text>

  <!-- Our detail is our difference -->
  <line class="rule" x1="106" y1="248" x2="380" y2="248"/>
  <line class="rule" x1="422" y1="248" x2="731" y2="248"/>
  <rect class="motif" x="388" y="230" width="28" height="30" rx="6" role="img" aria-label="Thumbs-up hand icon"/>
  <text class="value-light" x="108" y="335" font-size="78" textLength="293" lengthAdjust="spacingAndGlyphs">OUR</text>
  <text class="value-light" x="108" y="389" font-size="45" textLength="293" lengthAdjust="spacingAndGlyphs">DETAIL IS</text>
  <text class="value-slab" x="441" y="389" font-size="142" textLength="290" lengthAdjust="spacingAndGlyphs">OUR</text>
  <text class="value-slab" x="108" y="486" font-size="104" textLength="623" lengthAdjust="spacingAndGlyphs">DIFFERENCE.</text>

  <!-- Best intentions -->
  <line class="rule" x1="106" y1="505" x2="378" y2="505"/>
  <line class="rule" x1="462" y1="505" x2="731" y2="505"/>
  <rect class="motif" x="381" y="499" width="77" height="12" rx="5" role="img" aria-label="Pointing hand icon"/>
  <rect class="motif" x="46" y="544" width="69" height="18" rx="9" role="img" aria-label="Scroll flourish ornament"/>
  <rect class="motif" x="731" y="544" width="67" height="18" rx="9" role="img" aria-label="Scroll flourish ornament"/>
  <text class="value-bold" x="121" y="567" font-size="34" textLength="605" lengthAdjust="spacingAndGlyphs">BEST INTENTIONS. ALWAYS.</text>

  <!-- Turn up, turn on -->
  <line class="rule" x1="106" y1="599" x2="397" y2="599"/>
  <line class="rule" x1="451" y1="599" x2="738" y2="599"/>
  <circle class="motif" cx="424" cy="599" r="27"/>
  <text class="value-tech" x="133" y="690" font-size="58" textLength="578" lengthAdjust="spacingAndGlyphs">TURN UP, TURN ON!</text>
  <text class="value-tech" x="125" y="748" font-size="58" textLength="595" lengthAdjust="spacingAndGlyphs">MAKE ..IT HAPPEN!</text>

  <!-- Support & party -->
  <line class="rule" x1="106" y1="778" x2="388" y2="778"/>
  <line class="rule" x1="444" y1="778" x2="740" y2="778"/>
  <rect class="motif" x="398" y="753" width="38" height="30" rx="7" role="img" aria-label="Thumbs-up hand icon"/>
  <text class="value-script" x="108" y="838" font-size="64" textLength="624" lengthAdjust="spacingAndGlyphs">Support Like Family.</text>
  <text class="value-western" x="108" y="952" font-size="104" textLength="322" lengthAdjust="spacingAndGlyphs">PARTY</text>
  <text class="value-western" x="510" y="952" font-size="104" textLength="223" lengthAdjust="spacingAndGlyphs">LIKE</text>
  <rect class="motif" x="444" y="870" width="56" height="130" rx="14" role="img" aria-label="Silhouette of a cheering rock fan with arm raised"/>
  <line class="rule" x1="111" y1="985" x2="428" y2="985"/>
  <line class="rule" x1="512" y1="985" x2="738" y2="985"/>
  <text class="value-western" x="111" y="1107" font-size="130" textLength="661" lengthAdjust="spacingAndGlyphs">ROCKSTARS.</text>
  <line class="rule" x1="111" y1="1133" x2="743" y2="1133"/>
</svg>
</body>
</html>
```